TITLE: What Makes My Child’s Playing Talent Grow? SUB-TITLE: A Mother’s Plain Talk Manual for Coaching...

My book is for parents who have young children that are really into sports. My book empowers parents so they can motivate their children to succeed. It deals with sports psychology. Both my title and subtitle should be easy to read. Ideally, I would like a picture of young athlete(s) on the title. I have uploaded files of some books on Brindlemart that deal with the same subject. The last two files are 1) my company logo, please try to include these colors 2) an ebook cover I put together myself. You will notice an On-line bonus in the middle of the book, this Bonus needs to be on the cover.

Target Market(s)

Parents with children who play sports at a high level

Colors

Designer to choose colors to be used in the design.

Requirements
Must have
• Online Bonus feature as per my example.
• Dimensions: Pagelux = The ideal size of your eBook cover art is a height/width ratio of 1.6:1. This means that for every 1,000 pixels in width, the image should be 1,600 pixels in height.
Nice to have
• picture of a young athlete or young athletes

```html
<!DOCTYPE html>
<html lang="en">
<head>
<meta charset="utf-8">
<title>What Makes My Child’s Playing Talent Grow? – Cover</title>
<link href="https://fonts.googleapis.com/css2?family=Montserrat:wght@300;700;800;900&family=Oswald:wght@600&display=swap" rel="stylesheet">
<style>
  :root {
    --backdrop: #9a9ea1;
    --paper: #ffffff;
    --ink-brown: #3d3530;
    --ink-grey: #5a5552;
    --orange: #f0901e;
    --orange-deep: #d9620f;
    --orange-light: #f7a93a;
    --shade: #6d6a68;
  }
  * { margin: 0; padding: 0; box-sizing: border-box; }
  html, body { width: 1200px; height: 1200px; overflow: hidden; }
  body { background: var(--backdrop); position: relative; font-family: "Montserrat", sans-serif; }

  .cover {
    position: absolute; left: 256px; top: 50px;
    width: 688px; height: 1100px;
    background: var(--paper); overflow: hidden;
  }
  .title-lead {
    position: absolute; left: 0; right: 0; top: 74px;
    text-align: center; font-weight: 300; font-size: 36px;
    letter-spacing: 0.22em; color: var(--ink-grey); line-height: 1;
  }
  .title-main {
    position: absolute; left: 0; right: 0; top: 108px;
    text-align: center; font-weight: 900; font-size: 118px;
    letter-spacing: -0.05em; color: var(--ink-brown); line-height: 1;
  }
  .title-tail {
    position: absolute; left: 0; right: 0; top: 232px;
    text-align: center; font-weight: 800; font-size: 45px;
    letter-spacing: -0.05em; color: var(--orange); line-height: 1;
  }
  .athlete-photo {
    position: absolute; left: 160px; top: 330px; width: 420px; height: 530px;
    background: linear-gradient(160deg, #f4f4f4 0%, #e8c9a8 30%, #d39a6e 50%, #f2f2f2 68%, #3e8a4c 100%);
    border-radius: 40% 45% 10% 10% / 20% 25% 5% 5%;
    opacity: 0.9;
  }
  .bonus-seal { position: absolute; left: 420px; top: 305px; width: 180px; height: 180px; }
  .bonus-seal text { font-family: "Montserrat", sans-serif; text-anchor: middle; fill: var(--ink-brown); }

  .brand-mark {
    position: absolute; left: 74px; top: 758px; width: 156px; height: 156px;
    border-radius: 50%; background: var(--paper); border: 4px solid var(--orange);
    display: flex; align-items: center; justify-content: center; text-align: center;
    font-weight: 700; font-size: 17px; line-height: 1.2; color: var(--ink-brown);
    padding: 18px;
  }
  .subtitle-band { position: absolute; left: 0; top: 0; width: 688px; height: 1100px; }
  .subtitle {
    position: absolute; left: 190px; top: 862px; width: 470px;
    transform: rotate(-7.5deg); transform-origin: center;
    font-family: "Oswald", sans-serif; font-weight: 600; text-align: center;
    color: var(--ink-brown); text-transform: uppercase; line-height: 1.05;
  }
  .subtitle .l1 { font-size: 32px; }
  .subtitle .l2 { font-size: 30px; }
  .subtitle .l3 { font-size: 21px; }
</style>
</head>
<body>
  <main class="cover">
    <div class="title-lead">WHAT MAKES MY</div>
    <div class="title-main">CHILD’S</div>
    <div class="title-tail">PLAYING TALENT GROW?</div>

    <div class="athlete-photo" role="img" aria-label="Photo of a teenage runner in a white and green racing vest, running in profile"></div>

    <svg class="bonus-seal" viewBox="0 0 180 180" aria-label="Free online workshop bonus, $170 value">
      <polygon fill="var(--orange-deep)" points="90,2 100,14 114,6 119,21 135,18 135,33 150,35 145,50 160,58 150,70 163,82 150,92 160,106 145,112 150,128 135,128 134,144 119,140 112,155 100,146 90,160 80,146 68,155 61,140 46,144 45,128 30,128 35,112 20,106 30,92 17,82 30,70 20,58 35,50 30,35 45,33 45,18 61,21 66,6 80,14" transform="translate(0,9)"/>
      <circle cx="90" cy="90" r="62" fill="var(--orange)"/>
      <circle cx="90" cy="90" r="55" fill="none" stroke="var(--orange-light)" stroke-width="2"/>
      <text x="90" y="62" font-size="21" font-weight="700">FREE</text>
      <text x="90" y="73" font-size="8" font-weight="700">ONLINE</text>
      <text x="90" y="82" font-size="8" font-weight="700">WORKSHOP</text>
      <text x="90" y="113" font-size="34" font-weight="700">$170</text>
      <text x="90" y="130" font-size="17" font-weight="700">VALUE</text>
      <text x="90" y="140" font-size="6" font-weight="300">Details inside</text>
    </svg>

    <svg class="subtitle-band" viewBox="0 0 688 1100" aria-hidden="true">
      <polygon fill="var(--shade)" points="178,935 210,930 226,1012 195,1010"/>
      <polygon fill="var(--orange)" points="195,905 628,840 672,952 226,1012"/>
    </svg>
    <div class="brand-mark">Inner Play Coach Lumen</div>
    <div class="subtitle">
      <div class="l1">A Mother’s Plain Talk</div>
      <div class="l2">Manual for Coaching Confident,</div>
      <div class="l3">Focused and Resilient Athletes</div>
    </div>
  </main>
</body>
</html>
```